Maple Grove Schools | brand new stationery!

We need stationery design with our new logo! Our company updated it's name and image and we like to incorporate the new one on our stationery, business cards and email signature. We are looking for fresh, new ideas!
Industry: Childcare, Elementary and Middle School
Company Name: Maple Grove Schools
Tagline: Bright Futures Start Here
Main colors: Blue, white and a little yellow
Star shape is something new for us! Do you see a way to incorporate it as a design element?

```html
<!DOCTYPE html>
<html lang="en">
<head>
<meta charset="utf-8">
<title>Maple Grove Schools — Letterhead</title>
<link href="https://fonts.googleapis.com/css2?family=Lexend:wght@400;600&family=Arimo:ital,wght@1,700&display=swap" rel="stylesheet">
<style>
  :root {
    --canvas-bg: #ece6e6;
    --paper: #ffffff;
    --navy: #0f1d6e;
    --periwinkle: #8690c2;
    --sun: #fcc419;
    --sun-soft: #ffe08a;
    --ink: #1f2230;
    --tag-ink: #333846;
    --on-navy: #ffffff;
  }
  * { margin: 0; padding: 0; box-sizing: border-box; }
  html, body {
    width: 1200px;
    height: 1000px;
    overflow: hidden;
    background: var(--canvas-bg);
  }
  .canvas {
    position: relative;
    width: 1200px;
    height: 1000px;
  }
  .letterhead {
    position: absolute;
    left: 270px;
    top: 32px;
    width: 660px;
    height: 935px;
    background: var(--paper);
    box-shadow: 0 6px 24px rgba(60, 40, 40, 0.18);
  }
  .letterhead svg { display: block; width: 100%; height: 100%; }
  .brand-name { font-family: "Lexend", sans-serif; font-size: 27px; fill: var(--ink); }
  .brand-name .strong { font-weight: 600; }
  .brand-name .light { font-weight: 400; }
  .tagline { font-family: "Arimo", sans-serif; font-style: italic; font-weight: 700; font-size: 13px; fill: var(--tag-ink); }
  .contact-line { font-family: "Lexend", sans-serif; font-weight: 400; font-size: 8.5px; letter-spacing: 0.7px; fill: var(--on-navy); }
  .footer-name { font-family: "Lexend", sans-serif; font-size: 20px; fill: var(--ink); }
  .footer-name .strong { font-weight: 600; }
  .footer-name .light { font-weight: 400; }
</style>
</head>
<body>
<main class="canvas">
  <article class="letterhead">
    <svg viewBox="0 0 558 790" xmlns="http://www.w3.org/2000/svg">
      <defs>
        <linearGradient id="header-fade" x1="0" y1="0" x2="0" y2="1">
          <stop offset="0" stop-color="#8690c2"/>
          <stop offset="1" stop-color="#ffffff"/>
        </linearGradient>
        <linearGradient id="edge-fade" x1="0" y1="0" x2="0" y2="1">
          <stop offset="0" stop-color="#fcc419"/>
          <stop offset="1" stop-color="#ffe9a8"/>
        </linearGradient>
      </defs>

      <g class="header-band">
        <path class="header-edge" fill="url(#edge-fade)"
              d="M0 0 H558 V28 C490 42 452 62 434 112 L384 236 C368 276 340 280 312 280 C284 280 264 268 246 240 L186 140 C166 106 120 98 0 98 Z"/>
        <path class="header-fill" fill="url(#header-fade)"
              d="M0 0 H558 V18 C482 34 442 56 424 106 L374 228 C358 266 334 270 306 270 C280 270 262 258 242 230 L182 130 C162 100 118 92 0 92 Z"/>
      </g>

      <g class="brand-lockup">
        <circle cx="56" cy="44" r="13" fill="var(--navy)"/>
        <text class="brand-name" x="80" y="54"><tspan class="strong">Maple Grove</tspan> <tspan class="light">Schools</tspan></text>
        <text class="tagline" x="142" y="81">Bright Futures Start Here</text>
      </g>

      <g class="footer-band">
        <rect x="0" y="752" width="300" height="38" fill="var(--sun)"/>
        <text class="footer-name" x="20" y="777"><tspan class="strong">Maple Grove</tspan> <tspan class="light">Schools</tspan></text>
      </g>

      <g class="contact-panel">
        <path fill="var(--navy)"
              d="M266 790 C284 764 298 752 322 752 L346 752 C360 752 362 730 362 706 L362 598 C362 570 382 560 410 566 C440 572 456 590 476 600 C506 614 536 612 558 602 V790 Z"/>
        <path class="accent-star" fill="var(--sun)"
              d="M494 536 L505 561 L532 563 L511 580 L518 607 L494 592 L470 607 L477 580 L456 563 L483 561 Z"/>

        <g class="icon-pin" fill="var(--on-navy)">
          <path d="M386 651 a5 5 0 0 1 10 0 c0 4 -5 10 -5 10 c0 0 -5 -6 -5 -10 Z"/>
          <circle cx="391" cy="651" r="1.8" fill="var(--navy)"/>
        </g>
        <text class="contact-line" x="404" y="654">48 ELM ROAD</text>
        <text class="contact-line" x="404" y="664">UNIT 7</text>

        <path class="icon-phone" fill="var(--on-navy)"
              d="M385 678 c1 -1 3 -1 3 0 l2 3 c0 1 0 2 -1 2 c1 2 3 4 5 5 c0 -1 1 -1 2 -1 l3 2 c1 0 1 2 0 3 c-2 2 -5 1 -8 -1 c-3 -2 -5 -4 -7 -7 c-1 -2 -1 -5 1 -6 Z"/>
        <text class="contact-line" x="404" y="688">555-0142-318</text>

        <g class="icon-mail">
          <rect x="384" y="705" width="14" height="10" fill="var(--on-navy)"/>
          <path d="M384 705 L391 711 L398 705" fill="none" stroke="var(--navy)" stroke-width="1.2"/>
        </g>
        <text class="contact-line" x="404" y="713">HELLO@MGS.EDU</text>

        <g class="icon-globe" fill="none" stroke="var(--on-navy)" stroke-width="1">
          <circle cx="391" cy="735" r="7"/>
          <ellipse cx="391" cy="735" rx="3" ry="7"/>
          <path d="M384 735 H398 M385 731 H397 M385 739 H397"/>
        </g>
        <text class="contact-line" x="404" y="738">WWW.MGSCHOOLS.EDU</text>
      </g>
    </svg>
  </article>
</main>
</body>
</html>
```